A NEW UPDATED VERSION OF A 4"X9" RACK CARD

A NEW UPDATED VERSION OF A RACK CARD, THIS CARD IS 5 YEARS OLD AND WE WANT SOMETHING NEW AND FRESH AND MORE UPDATED TO TODAY. MARKET TO A YOUNGER CROWD. USE THE ATTACHED RACK CARD FOR THE INFO AND VERBAGE AND LOGO TO BE USED. DO NOT USE THE PICTURE OF THE BUILDIING, don't use the picture of the 2 guys. USED THE ATTACHED POST CARDS AS COLORS AND REFERENCE.

Target Market(s)

25-45

Industry/Entity Type

HOME INSPECTIONS

```html
<!DOCTYPE html>
<html lang="en">
<head>
<meta charset="utf-8">
<title>Summit Home Inspections – Rack Card</title>
<link rel="stylesheet" href="https://fonts.googleapis.com/css2?family=Oswald:wght@400;600;700&family=Roboto+Slab:wght@400;600;700&family=Tinos:wght@400;700&display=swap">
<style>
:root{
  --navy:#0b3c7d;
  --blue:#1560b0;
  --sky:#11a5e8;
  --red:#d8141c;
  --deep-red:#b3121b;
  --purple:#5b2a78;
  --yellow:#ffe11a;
  --ink:#222;
  --panel:#eeeff2;
  --stage:#3a3a3a;
}
*{box-sizing:border-box;margin:0;padding:0}
html,body{width:1200px;height:2487px;overflow:hidden;background:var(--stage)}
.stage{position:relative;width:1200px;height:2487px}
.card{position:absolute;top:613px;width:560px;height:1260px;background:#fff;overflow:hidden;font-family:"Tinos",serif;color:var(--ink)}
.card--front{left:20px}
.card--back{left:620px}

/* front */
.flag-wash{position:absolute;left:0;top:0;width:560px;height:420px;background:linear-gradient(180deg,#f3f4f7,#fff 70%)}
.headline{position:absolute;top:22px;left:0;width:100%;text-align:center;font-family:"Oswald",sans-serif;font-weight:700;font-size:78px;line-height:72px;letter-spacing:-1px;background:linear-gradient(180deg,var(--blue) 0%,var(--purple) 45%,var(--red) 90%);-webkit-background-clip:text;background-clip:text;color:transparent}
.side-band{position:absolute;top:330px;width:36px;height:400px;background:var(--navy)}
.side-band--left{left:0;border-top-right-radius:40px}
.side-band--right{right:0;border-top-left-radius:40px}
.services-panel{position:absolute;left:36px;top:370px;width:488px;height:530px;background:linear-gradient(180deg,#f5f6f8,var(--panel));border-radius:0 0 26px 26px;box-shadow:0 10px 14px -8px rgba(0,0,0,.25)}
.brand{position:absolute;left:0;top:230px;width:560px;display:flex;align-items:center;justify-content:center;gap:14px}
.brand__dot{width:34px;height:34px;border-radius:50%;background:var(--red)}
.brand__name{font-family:"Oswald",sans-serif;font-weight:700;font-size:44px;color:var(--navy);letter-spacing:1px}
.services-title{position:absolute;left:0;top:500px;width:560px;text-align:center;font-family:"Roboto Slab",serif;font-weight:700;font-size:40px;color:var(--blue);transform:rotate(-3deg)}
.service-grid{position:absolute;left:46px;top:580px;width:468px;display:grid;grid-template-columns:repeat(3,1fr);grid-template-rows:158px 158px}
.service{display:flex;flex-direction:column;align-items:center;text-align:center;font-family:"Roboto Slab",serif;font-size:15px;line-height:18px;color:#333;padding-top:4px}
.service:nth-child(-n+3){border-bottom:1px dashed #9ab}
.service:not(:nth-child(3n)){border-right:1px dashed #9ab}
.service:nth-child(n+4){padding-top:14px}
.service__icon{width:80px;height:80px;border-radius:50%;background:#fff;border:4px solid transparent;background-image:linear-gradient(#fff,#fff),linear-gradient(135deg,var(--blue),var(--red));background-origin:border-box;background-clip:padding-box,border-box;box-shadow:0 4px 8px rgba(0,0,0,.2);display:flex;align-items:center;justify-content:center;margin-bottom:8px}
.service__icon svg{width:40px;height:40px;fill:none;stroke:#333;stroke-width:2}
.tabs{position:absolute;left:40px;top:940px;width:490px;height:150px}
.tab{position:absolute;width:118px;border-radius:10px 10px 0 0;color:#fff;font-family:"Roboto Slab",serif;font-size:15px;line-height:17px;text-align:center;padding-top:30px;box-shadow:0 8px 10px -6px rgba(0,0,0,.4)}
.tab svg{display:block;margin:10px auto 0;width:34px;height:34px;fill:none;stroke:rgba(255,255,255,.7);stroke-width:2}
.tab--mold{left:2px;top:22px;height:128px;background:var(--navy)}
.tab--radon{left:116px;top:0;height:138px;background:var(--red);padding-top:80px}
.tab--wdo{left:230px;top:44px;height:114px;background:var(--blue);padding-top:20px}
.tab--water{left:345px;top:0;height:138px;background:var(--sky);padding-top:60px}
.tagline{position:absolute;left:14px;top:1128px;width:532px;height:30px;background:linear-gradient(90deg,rgba(21,96,176,.85),rgba(255,255,255,.4) 50%,rgba(216,20,28,.85));text-align:center;font-family:"Oswald",sans-serif;font-size:18px;line-height:30px;color:var(--yellow);letter-spacing:.5px}
.tagline span{color:#fff;font-size:12px;letter-spacing:2px}
.call{position:absolute;left:0;top:1166px;width:560px;text-align:center;font-family:"Oswald",sans-serif;font-size:32px;color:#333;font-weight:400;display:flex;justify-content:center;align-items:center;gap:8px}
.call strong{font-weight:600;color:#222}
.call__phone{width:30px;height:30px;border-radius:50%;background:var(--red);display:inline-flex;align-items:center;justify-content:center}
.call__phone svg{width:18px;height:18px;fill:#fff}
.web{position:absolute;left:105px;bottom:0;width:350px;height:40px;background:var(--blue);clip-path:polygon(8% 0,92% 0,100% 100%,0 100%);color:#fff;text-align:center;font-family:"Oswald",sans-serif;font-weight:600;font-size:18px;line-height:44px}

/* back */
.hero{position:absolute;left:0;top:0;width:560px;height:260px;background:linear-gradient(100deg,var(--navy) 0%,var(--purple) 55%,var(--red) 100%);clip-path:ellipse(95% 100% at 50% 0)}
.hero__title{position:absolute;left:0;top:18px;width:560px;text-align:center;font-family:"Oswald",sans-serif;font-weight:700;font-size:52px;line-height:54px;color:var(--yellow)}
.hero__rule{position:absolute;left:190px;top:150px;width:180px;height:1px;background:rgba(255,255,255,.5)}
.hero__sub{position:absolute;left:0;top:164px;width:560px;text-align:center;color:#fff;font-size:18px;line-height:22px}
.hero__sub b{font-size:22px;letter-spacing:.5px}
.frame{position:absolute;left:36px;top:205px;width:488px;height:660px;border:1.5px solid #777;border-radius:18px;border-top:none}
.frame__dot{position:absolute;left:-7px;width:12px;height:12px;border-radius:50%;background:var(--red)}
.tagline-blue{position:absolute;left:0;top:283px;width:560px;text-align:center;font-family:"Roboto Slab",serif;font-weight:600;font-size:23px;color:var(--blue)}
.why{position:absolute;left:0;top:348px;width:560px;text-align:center;font-family:"Roboto Slab",serif;font-weight:700;font-size:40px;color:var(--deep-red)}
.reasons{position:absolute;left:72px;top:408px;width:420px;text-align:center;font-size:16.5px;line-height:19px}
.reasons p{margin-bottom:19px}
.cta{position:absolute;top:760px;width:198px;height:180px;display:flex;align-items:center;justify-content:center;text-align:center;font-family:"Roboto Slab",serif;font-size:20px;line-height:24px;color:var(--yellow);padding-top:40px;box-shadow:0 10px 10px -8px rgba(0,0,0,.35)}
.cta--visit{left:77px;background:var(--navy)}
.cta--honest{left:284px;background:var(--red);font-weight:600}
.cta b{font-weight:700}
.cta__stars{position:absolute;top:14px;left:0;width:100%;color:#fff;font-size:22px;letter-spacing:4px}
.partner{position:absolute;left:60px;top:1000px;width:440px;display:flex;align-items:center;gap:24px}
.partner .brand__name{font-size:26px;line-height:30px;text-align:center}
.partner__logo{display:flex;align-items:center;gap:10px;width:200px}
.partner__logo .brand__dot{width:22px;height:22px;flex:none}
.partner__text{font-size:16px;line-height:21px}
</style>
</head>
<body>
<main class="stage">

  <section class="card card--front" aria-label="Rack card front">
    <div class="flag-wash" role="img" aria-label="Soft waving flag texture behind the headline"></div>
    <h1 class="headline">INSPECTING FOR<br>THE UNEXPECTED</h1>
    <div class="side-band side-band--left"></div>
    <div class="side-band side-band--right"></div>
    <div class="services-panel"></div>
    <div class="brand"><span class="brand__dot"></span><span class="brand__name">SUMMIT HOME INSPECTIONS</span></div>
    <h2 class="services-title">OUR SERVICES</h2>
    <div class="service-grid">
      <div class="service"><span class="service__icon"><svg viewBox="0 0 40 40"><path d="M6 20 20 8l14 12M10 17v16h20V17M16 33v-9h8v9"/></svg></span>Home<br>Inspections</div>
      <div class="service"><span class="service__icon"><svg viewBox="0 0 40 40"><path d="M10 18a10 10 0 0 1 20 0zM8 18h24M12 34v-8h16v8"/></svg></span>Builder's Warranty<br>Inspections</div>
      <div class="service"><span class="service__icon"><svg viewBox="0 0 40 40"><path d="M6 14h20a4 4 0 1 0-4-4M6 20h28a4 4 0 1 1-4 4M6 26h14"/></svg></span>Wind<br>Mitigations</div>
      <div class="service"><span class="service__icon"><svg viewBox="0 0 40 40"><path d="M20 6l6 6-6 6-6-6zM20 22l6 6-6 6-6-6zM12 14l6 6-6 6-6-6zM28 14l6 6-6 6-6-6z"/></svg></span>4-point<br>Inspections</div>
      <div class="service"><span class="service__icon"><svg viewBox="0 0 40 40"><path d="M10 8h20v28H10zM16 5h8v6h-8zM14 17h4v4h-4zM14 26h4v4h-4zM21 19h6M21 28h6"/></svg></span>Pre-listing<br>Inspections</div>
      <div class="service"><span class="service__icon"><svg viewBox="0 0 40 40"><path d="M12 6h16v30H12zM6 36h28M16 11h3M21 11h3M16 17h3M21 17h3M16 23h3M21 23h3M18 36v-6h4v6"/></svg></span>Commercial<br>Inspections</div>
    </div>
    <div class="tabs">
      <div class="tab tab--mold">Mold<br>Testing<svg viewBox="0 0 34 34"><circle cx="12" cy="20" r="6"/><circle cx="24" cy="12" r="5"/><circle cx="24" cy="26" r="4"/></svg></div>
      <div class="tab tab--wdo">WDO/Termite<br>Inspections<svg viewBox="0 0 34 34"><ellipse cx="17" cy="19" rx="5" ry="9"/><path d="M12 14 5 10M12 20H4M12 25l-7 4M22 14l7-4M22 20h8M22 25l7 4"/></svg></div>
      <div class="tab tab--radon">Radon<br>Testing</div>
      <div class="tab tab--water">Water Quality<br>Testing</div>
    </div>
    <div class="tagline"><span>★★★</span> MULTI - INSPECTIONS FIRM <span>★★★</span></div>
    <div class="call">CALL NOW <span class="call__phone"><svg viewBox="0 0 24 24"><path d="M6.6 10.8a15 15 0 0 0 6.6 6.6l2.2-2.2c.3-.3.7-.4 1-.2 1.1.4 2.3.6 3.6.6.6 0 1 .4 1 1V20c0 .6-.4 1-1 1A17 17 0 0 1 3 4c0-.6.4-1 1-1h3.5c.6 0 1 .4 1 1 0 1.3.2 2.5.6 3.6.1.3 0 .7-.2 1z"/></svg></span><strong>1-800-555-0147</strong></div>
    <div class="web">WWW.SUMMITHOMEINSPECT.COM</div>
  </section>

  <section class="card card--back" aria-label="Rack card back">
    <div class="hero" role="img" aria-label="Flag-inspired blue to red header with stars"></div>
    <h1 class="hero__title">SUMMIT<br>HOME INSPECTIONS</h1>
    <div class="hero__rule"></div>
    <p class="hero__sub">PROFESSIONAL &amp; PROMPT SERVICE<br><b>GUARANTEED</b></p>
    <div class="frame">
      <span class="frame__dot" style="top:198px"></span>
      <span class="frame__dot" style="top:310px"></span>
      <span class="frame__dot" style="top:384px"></span>
      <span class="frame__dot" style="top:478px"></span>
    </div>
    <h2 class="tagline-blue">Florida's # 1 Inspection Company</h2>
    <h2 class="why">WHY US ?</h2>
    <div class="reasons">
      <p>All Summit Home Inspections Inspectors are trained to the highest standards in the industry and are equipped with the most advanced tools to ensure that all customers are getting a great inspec-tion as well asgetting a great value.</p>
      <p>Our Full Home inspections include a comprehensive visual inspection of the interior and exterior of the home looking at over 1,400 different items.</p>
      <p>We inspect and test all accessible components of the home, inputting our findings into a report that is honest and easy to understand and full of pictures for easy reference.</p>
      <p>We base our pricing on total square footage of the home and do not charge extra to inspect pools, attics, roofs or crawlspaces.</p>
    </div>
    <div class="cta cta--visit"><span class="cta__stars">★★★★</span><span>VISIT OUR<br><b>WEBSITE</b> TO<br><b>BOOK AN<br>INSPECTION</b></span></div>
    <div class="cta cta--honest"><span class="cta__stars">★★★★</span><span>YOUR HONEST<br>AND FRIENDLY<br><b>HOME<br>INSPECTORS</b></span></div>
    <div class="partner">
      <div class="partner__logo"><span class="brand__dot"></span><span class="brand__name">SUMMIT HOME INSPECTIONS</span></div>
      <p class="partner__text">WOD (Termite inspections) performed by Northgate Pest Defense and is included with every full home inspection.</p>
    </div>
    <div class="tagline"><span>★★★</span> THE BOOK YOUR INSPECTIONS <span>★★★</span></div>
    <div class="call">CALL NOW <span class="call__phone"><svg viewBox="0 0 24 24"><path d="M6.6 10.8a15 15 0 0 0 6.6 6.6l2.2-2.2c.3-.3.7-.4 1-.2 1.1.4 2.3.6 3.6.6.6 0 1 .4 1 1V20c0 .6-.4 1-1 1A17 17 0 0 1 3 4c0-.6.4-1 1-1h3.5c.6 0 1 .4 1 1 0 1.3.2 2.5.6 3.6.1.3 0 .7-.2 1z"/></svg></span><strong>1-800-555-0147</strong></div>
    <div class="web">WWW.SUMMITHOMEINSPECT.COM</div>
  </section>

</main>
</body>
</html>
```